Lanternleaf - Fresh Asian Cuisine Menu

We need to redo our menu to include pictures of food items. Our restaurant is vibrant, trendy, upscale Chinese cuisine

Requirements
Must have
• Must fit on 8.5x11 paper. We can remove the About Us section if needed but menu cannot be more than 6 pages total. Must include pictures of menu items

```html
<!DOCTYPE html>
<html lang="en">
<head>
<meta charset="utf-8">
<title>Lanternleaf - Fresh Asian Cuisine Menu</title>
<link href="https://fonts.googleapis.com/css2?family=Exo+2:wght@300&family=Roboto+Condensed:wght@300;700&family=Fira+Sans:wght@700&display=swap" rel="stylesheet">
<style>
:root{
  --page:#ffffff;
  --paper:#fbf5ee;
  --frame:#c8102e;
  --orange:#e8981c;
  --banner:#c8102e;
  --banner-text:#f7c33b;
  --ink:#1d1d1d;
  --muted:#6f6a66;
  --blossom:#f1d3cd;
}
*{margin:0;padding:0;box-sizing:border-box}
html,body{width:1200px;height:1200px;overflow:hidden;background:var(--page)}
.canvas{position:relative;width:1200px;height:1200px;background:var(--page)}
.menu-spread{position:absolute;left:0;top:210px;width:1200px;height:756px;background:var(--paper);overflow:hidden}
.frame{position:absolute;inset:0;pointer-events:none}
.splash{position:absolute;left:190px;top:0;width:560px;height:220px;border-radius:0 0 50% 45%;background:radial-gradient(ellipse at 55% 40%,rgba(224,66,76,.85),rgba(240,170,170,.35) 65%,rgba(251,245,238,0) 80%)}
.photo{position:absolute}
.photo-side{left:266px;top:0;width:106px;height:104px;background:linear-gradient(150deg,#3a2a20,#c84a2a 55%,#9fcf7a)}
.photo-main{left:426px;top:-72px;width:300px;height:300px;border-radius:50%;background:radial-gradient(circle,#8a2a14 0%,#b9401e 45%,#d8632a 62%,#f4efe8 66%,#ffffff 72%)}
.photo-dumplings{left:726px;top:0;width:156px;height:104px;background:linear-gradient(160deg,#f3efe6,#e6b660 50%,#c9893a)}
.branch{position:absolute;background:linear-gradient(120deg,rgba(241,211,205,0),rgba(241,211,205,.8),rgba(241,211,205,0))}
.branch-center{left:420px;top:420px;width:220px;height:336px}
.branch-right{left:1000px;top:470px;width:190px;height:140px}
.pig{position:absolute;left:50px;top:670px;width:92px;height:62px;border-radius:46% 50% 44% 48%;background:var(--blossom)}
.lantern{position:absolute;left:1098px;top:50px;width:48px;height:70px;border-radius:50% 50% 40% 40%;background:radial-gradient(circle,#fff 30%,var(--frame) 34%,var(--frame) 60%,transparent 62%)}
.brand-top{position:absolute;left:30px;top:40px;display:flex;align-items:center;gap:6px}
.brand-top .dot{width:38px;height:38px;border-radius:50%;background:var(--frame)}
.brand-top span{font-family:"Roboto Condensed",sans-serif;font-weight:700;font-size:12px;color:var(--frame)}
.heading{position:absolute;font-family:"Exo 2",sans-serif;font-weight:300;color:var(--orange);letter-spacing:2px;line-height:.92}
.heading-appetizers{left:40px;top:136px;font-size:68px}
.heading-entrees{left:800px;top:148px;font-size:70px}
.banner{position:absolute;left:828px;width:156px;height:25px;background:var(--banner);border:2px solid #e9b04a;color:var(--banner-text);font-family:"Fira Sans",sans-serif;font-weight:700;font-size:15px;display:flex;align-items:center;justify-content:center}
.banner-chef{top:244px}
.banner-beef{top:456px}
.column{position:absolute;width:238px;display:flex;flex-direction:column;gap:9px}
.col-a{left:38px;top:276px;gap:14px}
.col-b{left:314px;top:276px;gap:15px}
.col-c{left:654px;top:292px}
.col-d{left:926px;top:292px}
.col-e{left:654px;top:510px}
.col-f{left:926px;top:510px}
.item h3{font-family:"Roboto Condensed",sans-serif;font-weight:700;font-size:10.5px;color:var(--ink)}
.item p{font-family:"Roboto Condensed",sans-serif;font-weight:300;font-size:9.6px;line-height:1.3;color:var(--muted);text-align:justify}
.addon{font-family:"Roboto Condensed",sans-serif;font-weight:700;font-size:10.5px;color:var(--ink)}
.brand-bottom{position:absolute;right:46px;top:706px;font-family:"Roboto Condensed",sans-serif;font-weight:700;font-size:18px;color:var(--ink)}
</style>
</head>
<body>
<div class="canvas">
  <section class="menu-spread">
    <div class="splash" role="img" aria-label="Red ink brush splash behind the food"></div>
    <div class="photo photo-side" role="img" aria-label="Photo of a small dish of minced spicy pork with vegetables"></div>
    <div class="photo photo-main" role="img" aria-label="Photo of Sichuan spicy beef in chili oil with cilantro"></div>
    <div class="photo photo-dumplings" role="img" aria-label="Photo of pan fried dumplings on a plate"></div>
    <div class="branch branch-center" role="img" aria-label="Faint blossom branch decoration"></div>
    <div class="branch branch-right" role="img" aria-label="Faint blossom branch decoration"></div>
    <div class="pig" role="img" aria-label="Soft pink zodiac pig decoration"></div>
    <div class="lantern" role="img" aria-label="Red hanging lantern decoration"></div>

    <svg class="frame" width="1200" height="756" viewBox="0 0 1200 756">
      <rect x="18" y="18" width="1164" height="720" fill="none" stroke="#c8102e" stroke-width="2"/>
      <rect x="24" y="24" width="1152" height="708" fill="none" stroke="#c8102e" stroke-width="1"/>
    </svg>

    <div class="brand-top"><div class="dot"></div><span>Lanternleaf</span></div>

    <h1 class="heading heading-appetizers">APPE<br>TIZERS</h1>
    <h1 class="heading heading-entrees">ENTREES</h1>

    <div class="column col-a">
      <div class="item"><h3>Edamame</h3><p>Seasoned &amp; boiled soy bean.</p></div>
      <div class="item"><h3>Scallion Pancakes</h3><p>Traditional Chinese flatbread folded with oil and minced scallions pan fried.</p></div>
      <div class="item"><h3>Lanternleaf Lettuce Wraps</h3><p>Seasoned ground chicken drizzled with our top secret homemade sauce served with lettuce wraps.</p></div>
      <div class="item"><h3>Salt &amp; Pepper Calamari</h3><p>Crispy Calamari with Green &amp; red peppers and onions.</p></div>
      <div class="item"><h3>Buddha Bang Shrimp</h3><p>Crispy fried shrimp tossed in our creamy spicy sauce.</p></div>
      <div class="item"><h3>Drunken Chicken</h3><p>Chicken, Thai chili in a house made spicy sauce.</p></div>
      <div class="item"><h3>Sichuan Spiced Beef</h3><p>Beef Shank, beef tripe, cilantro, peanuts and celery.</p></div>
      <div class="item"><h3>Beef Crispy Bottom Bao</h3><p>Pan fried crispy bottom Bao, stuffed with beef, drizzled with scallion and sesame (Fresh made to order, takes at least 20 mins to serve).</p></div>
      <div class="addon">add Shrimp $1</div>
    </div>

    <div class="column col-b">
      <div class="item"><h3>Crispy Mala Beef Jerky</h3><p>Dry fried shredded beef with various peppers in sesame and peppercorn oil.</p></div>
      <div class="item"><h3>Fried Chicken Dumplings (6)</h3><p>Chinese dumpling stuffed with Chicken, Shiitake mushrooms and bamboo shoots.</p></div>
      <div class="item"><h3>Red Oil Dumplings (6)</h3><p>Chicken filled dumplings in Sichuan red oil sauce drizzled with sesame.</p></div>
      <div class="item"><h3>Pork Egg Rolls (2)</h3><p>Hand rolled with julienned veggies with our sweet n' sour mustard sauce.</p></div>
      <div class="item"><h3>Vegetarian Spring Rolls (3)</h3><p>Traditional Asian Roll served with a sweet chili sauce.</p></div>
      <div class="item"><h3>Garlic Cucumber Salad</h3><p>Sliced cucumber with a garlic vinaigrette.</p></div>
      <div class="item"><h3>Hot n' Sour Soup</h3><p>Tangy broth with Bamboo shoot, wood ear mushrooms, tofu, egg and carrots.</p></div>
      <div class="item"><h3>West Lake Soup</h3><p>Light creamy soup with ground beef, diced Shiitake mushroom, tofu, bamboo shoots, egg white and cilantro.</p></div>
    </div>

    <div class="banner banner-chef">Chef Specialties</div>
    <div class="banner banner-beef">Beef &amp; Pork</div>

    <div class="column col-c">
      <div class="item"><h3>Jasmine Tea Smoked Duck</h3><p>Boneless half duck served with thinly sliced cucumber, scallion, house made duck sauce and soft flour wrap.</p></div>
      <div class="item"><h3>Sizzling Cumin' Lamb</h3><p>Tender pieces of lamb rubbed in cumin, Sichuan peppers, red and green bell peppers and onions.</p></div>
      <div class="item"><h3>Chef Lo's Spicy Beef</h3><p>Angus beef in house made green peppercorn sauce with Chinese cabbage, sprouts and celery garnished with fresh Sichuan peppercorn, Thai chili and cilantro.</p></div>
    </div>

    <div class="column col-d">
      <div class="item"><h3>Chef Lo's Spicy Fish</h3><p>Fish filet in house made green peppercorn sauce with Chinese cabbage, sprouts and celery garnished with fresh Sichuan peppercorn, Thai chili and cilantro.</p></div>
      <div class="item"><h3>General Tso's Scallops</h3><p>The perfect combination of tender scallops marinated in a sweet chili sauce with broccoli and red peppers.</p></div>
    </div>

    <div class="column col-e">
      <div class="item"><h3>Dancing Beef</h3><p>Angus Beef slices on a bed of sizzling rice crackers, black peppercorn and Thai chili.</p></div>
      <div class="item"><h3>Oyster Beef</h3><p>Tender cuts of steak wok fried with onions and marinated in a homemade oyster sauce.</p></div>
      <div class="item"><h3>Double Pepper Beef</h3><p>Angus steak with peppercorn, Thai chili, Serrano pepper and tofu and rice noodles.</p></div>
      <div class="item"><h3>Black Pepper Steak</h3><p>Tender cuts of steak mixed with onions and red and green bell peppers.</p></div>
    </div>

    <div class="column col-f">
      <div class="item"><h3>Singapore Baby Back Ribs</h3><p>Tender Baby back ribs rubbed in a Thai inspired sweet tangy glaze.</p></div>
      <div class="item"><h3>Dancing Pork Belly</h3><p>Braised Pork Belly on sizzling rice cracker.</p></div>
      <div class="item"><h3>Twice Cooked Pork</h3><p>Stir fried Pork Belly slices with leek and fermented black beans.</p></div>
    </div>

    <div class="brand-bottom">Lanternleaf</div>
  </section>
</div>
</body>
</html>
```